Brookvale Rendering Wordpress Design

I would like a design for my friends company. He has just had his logo designed and really likes the following website.

www.tlb-rendering.co.uk

Something similar to this design would be ideal but open to additional ideas. The website shown has all the relevant content.

We have 20 years of experience and can provide a number of photos for work we have done.

More photos will be provided upon request.

Target Market(s)

Homeowners

Industry/Entity Type

Trade

Font styles to use
Sans Serif

Colors
3176b5
85cae6
85abd2
eaf1f7

Requirements
Must have
• look at www.tlb-rendering.co.uk
Nice to have
Should not have
• N/A

```html
<!DOCTYPE html>
<html lang="en">
<head>
<meta charset="utf-8">
<title>Brookvale Rendering</title>
<link href="https://fonts.googleapis.com/css2?family=Montserrat:wght@400;500;600&family=Open+Sans:wght@400;600&family=Cabin:wght@500;600&display=swap" rel="stylesheet">
<style>
:root{
  --blue:#3176b5;
  --sky:#85cae6;
  --mid:#85abd2;
  --pale:#eaf1f7;
  --ink:#4a4a4a;
  --grey:#8a8a8a;
  --slate:#3e5b79;
  --dark:#333536;
  --green:#2db83d;
}
*{box-sizing:border-box;margin:0;padding:0}
html,body{width:1200px;height:3416px;overflow:hidden}
body{position:relative;font-family:"Open Sans",Arial,sans-serif;color:var(--ink);background:#fff}
.abs{position:absolute}

/* top bar */
.topbar{left:0;top:0;width:1200px;height:32px;background:var(--blue);color:#fff;font-size:12px}
.topbar span{position:absolute;top:8px;display:flex;align-items:center;gap:5px}

/* header */
.header{left:0;top:32px;width:1200px;height:103px;background:#fff}
.brand{left:130px;top:14px;width:193px;height:72px;display:flex;align-items:center;gap:8px}
.brand-mark{width:14px;height:14px;background:var(--blue)}
.brand-name{font-family:"Montserrat",sans-serif;font-weight:600;font-size:17px;color:var(--blue);line-height:1.1}
.nav a{position:absolute;top:52px;font-family:"Montserrat",sans-serif;font-size:11px;font-weight:500;color:#555;text-decoration:none;text-transform:uppercase}
.nav a.active{color:var(--blue)}

/* share squares */
.social{left:0;top:97px;width:32px;z-index:5}
.social i{display:block;width:32px;height:30px;margin-bottom:2px}

/* hero */
.hero{left:0;top:135px;width:1200px;height:373px;background:linear-gradient(100deg,#5a4a3a 0%,#7d6a55 35%,#8c8276 60%,#5c5047 100%)}
.hero-title{left:166px;top:38px;color:#fff;font-family:"Montserrat",sans-serif;font-size:46px;line-height:1;font-weight:400}
.hero-sub{left:166px;top:82px;color:var(--sky);font-family:"Montserrat",sans-serif;font-size:29px;font-weight:500}
.hero label{position:absolute;left:169px;color:#fff;font-size:12px}
.hero .field{position:absolute;left:170px;width:353px;height:31px;background:#fff}
.hero .submit{position:absolute;left:257px;top:268px;width:170px;height:30px;background:var(--green);color:#fff;font-size:13px;display:flex;align-items:center;justify-content:center}
.arrow-box{position:absolute;top:170px;width:34px;height:56px;border:1px solid #fff;display:flex;align-items:center;justify-content:center}

/* intro band */
.band{left:0;top:508px;width:1200px;height:144px;background:#3a3b3d;text-align:center}
.band h2{margin-top:30px;color:var(--sky);font-family:"Montserrat",sans-serif;font-size:32px;font-weight:500}
.band p{margin-top:8px;color:#e6e6e6;font-size:14.5px;line-height:21px}

/* section headings */
.sec-title{width:1200px;left:0;text-align:center;font-family:"Montserrat",sans-serif;font-weight:500;font-size:32px;color:#4a4a4a}
.sec-lead{width:1200px;left:0;text-align:center;font-size:14.5px;line-height:21px;color:var(--grey)}

/* services */
.service{width:300px}
.service .icon{position:absolute;left:0;top:0;width:69px;height:69px;border-radius:50%;background:var(--pale);display:flex;align-items:center;justify-content:center}
.service h3{position:absolute;left:86px;top:0;font-family:"Cabin",sans-serif;font-weight:600;font-size:18.5px;color:var(--blue)}
.service p{position:absolute;left:86px;top:36px;width:210px;font-size:11px;line-height:18.5px;color:#777}

/* video */
.video-sec{left:0;top:1217px;width:1200px;height:389px;background:var(--slate)}
.video{left:130px;top:61px;width:495px;height:276px;background:linear-gradient(120deg,#d8d8d8,#eeeeee 40%,#c49a6c 70%,#e8e8e8)}
.play{left:217px;top:112px;width:53px;height:37px;border-radius:8px;background:#1c1c1c;display:flex;align-items:center;justify-content:center}
.video-sec h2{position:absolute;left:654px;top:86px;width:340px;color:var(--sky);font-family:"Montserrat",sans-serif;font-weight:500;font-size:31px;line-height:30px}
.video-sec p{position:absolute;left:654px;top:164px;width:415px;color:#fff;font-size:12.5px;line-height:18.5px}
.quote-btn{position:absolute;left:774px;top:260px;width:145px;height:30px;background:var(--blue);color:#fff;font-size:12px;display:flex;align-items:center;justify-content:center;gap:6px}

/* recent work */
.work-sec{left:0;top:1606px;width:1200px;height:712px;background:#f5f5f5}
.grid{left:130px;top:177px;width:951px;height:475px;display:grid;grid-template-columns:repeat(4,1fr);grid-template-rows:1fr 1fr;gap:2px}
.grid div{width:100%;height:100%}

/* partners */
.partners-title{left:0;top:2385px;width:1200px;text-align:center}
.partners-title span{font-family:"Montserrat",sans-serif;font-weight:500;font-size:33px;color:#9a9a9a;background:#fff;padding:0 16px;position:relative}
.rule{left:130px;top:2406px;width:951px;height:1px;background:#e3e3e3}
.sq-btn{position:absolute;width:33px;height:33px;border:1px solid #cfcfcf;background:#fff;display:flex;align-items:center;justify-content:center}
.partner{top:2500px;height:60px;display:flex;align-items:center;gap:8px;font-family:"Montserrat",sans-serif;font-weight:600;font-size:17px;color:var(--blue)}
.partner i{width:14px;height:14px;background:var(--blue);display:block}

/* testimonials */
.testi{left:0;top:2628px;width:1200px;height:318px;background:#ebedef;text-align:center}
.testi h2{margin-top:64px;font-family:"Montserrat",sans-serif;font-weight:500;font-size:26px;color:var(--blue)}
.testi p{margin:22px auto 0;width:800px;font-size:12.5px;line-height:21px;color:#777}
.testi .who{margin-top:18px;font-family:"Montserrat",sans-serif;font-size:15px;color:#666}
.testi .role{margin-top:4px;font-size:12px;color:#888}

/* footer */
.footer{left:0;top:2946px;width:1200px;height:470px;background:var(--dark);color:#fff}
.footer h4{position:absolute;top:64px;font-family:"Montserrat",sans-serif;font-weight:500;font-size:16px}
.f-menu{position:absolute;left:131px;top:100px;font-size:11.5px;line-height:24px}
.post{position:absolute;left:330px;display:flex;align-items:center;gap:10px;width:230px;height:58px}
.post i{flex:none;width:58px;height:58px;border-radius:50%}
.post span{font-size:12px;line-height:18px}
.tweets{position:absolute;left:625px;top:97px;width:202px;height:224px;background:#6d9fcf;color:#fff;overflow:hidden}
.tweets .top{padding:7px 10px 0;font-size:8px;line-height:11px}
.tweets .name{padding:0 10px;font-size:14px;line-height:19px;font-weight:600}
.tweets ul{list-style:none;margin:4px 6px 0;background:#fff;height:158px;padding:2px 5px;overflow:hidden}
.tweets li{display:flex;gap:6px;font-size:8.5px;line-height:11px;color:#555;padding:5px 0;border-bottom:1px solid #e2e2e2}
.tweets li:last-child{border-bottom:0}
.tweets li i{flex:none;width:22px;height:22px;background:#b9b9b9}
.tweets li b{color:var(--blue);font-weight:600}
.tweets .bottom{display:flex;justify-content:space-between;height:25px;align-items:center;padding:0 10px;font-size:9px;font-weight:600}
.contact{position:absolute;left:916px;top:103px;font-size:11px;line-height:16px}
.copy{position:absolute;left:0;top:407px;width:1200px;text-align:center;font-size:10.5px}
</style>
</head>
<body>

<div class="abs topbar">
  <span style="left:130px"><svg width="12" height="9" viewBox="0 0 12 9"><rect x=".5" y=".5" width="11" height="8" fill="none" stroke="#fff"/><path d="M.5 .5l5.5 4 5.5-4" fill="none" stroke="#fff"/></svg>hello@brookvalerendering.co.uk</span>
  <span style="left:344px"><svg width="9" height="12" viewBox="0 0 9 12"><path d="M2 1c-1 1-1.5 3 0 6s3.5 4.5 5 4l1-1.5-2-1.5-1 1c-1-1-2-3-2-4l1-.5L3.5 1z" fill="#fff"/></svg>01632 960 456</span>
</div>

<div class="abs header">
  <div class="abs brand"><span class="brand-mark"></span><span class="brand-name">Brookvale<br>Rendering</span></div>
  <nav class="nav">
    <a class="active" style="left:373px">Home</a>
    <a style="left:432px">About</a>
    <a style="left:493px">Services ▾</a>
    <a style="left:569px">News &amp; Updates</a>
    <a style="left:685px">Contact Us</a>
  </nav>
  <svg class="abs" style="left:1069px;top:54px" width="11" height="11" viewBox="0 0 11 11"><circle cx="4.5" cy="4.5" r="3.5" fill="none" stroke="#666" stroke-width="1.5"/><path d="M7 7l3 3" stroke="#666" stroke-width="1.5"/></svg>
</div>

<section class="abs hero" role="img" aria-label="Tradesman in a yellow hard hat standing in front of a stone house under renovation">
  <div class="abs hero-title">Welcome to</div>
  <div class="abs hero-sub">Brookvale Rendering</div>
  <label style="top:132px">Your name:</label><div class="field" style="top:150px"></div>
  <label style="top:198px">Your email:</label><div class="field" style="top:217px"></div>
  <div class="submit">Submit</div>
  <div class="arrow-box" style="left:37px"><svg width="8" height="12"><path d="M6 1L1 6l5 5" fill="none" stroke="#fff" stroke-width="1.5"/></svg></div>
  <div class="arrow-box" style="left:1128px"><svg width="8" height="12"><path d="M2 1l5 5-5 5" fill="none" stroke="#fff" stroke-width="1.5"/></svg></div>
</section>

<div class="abs social">
  <i style="background:#3b5998"></i><i style="background:#3aa8d8"></i><i style="background:#d34836"></i><i style="background:#c9202a"></i>
</div>

<section class="abs band">
  <h2>We are company county Rendering in city</h2>
  <p>Lorem ipsum dolor sit amet, consectetur adipiscing elit. Etiam auctor tortor tellus, ut consectetur arcu.<br>Nulla consequat egestas dapibus.</p>
</section>

<h2 class="abs sec-title" style="top:692px">What We Do</h2>
<p class="abs sec-lead" style="top:744px">Lorem ipsum dolor sit amet, consectetur adipiscing elit. Etiam auctor tortor tellus, ut<br>consectetur arcu. Nulla consequat egestas dapibus.</p>

<div class="abs service" style="left:129px;top:832px">
  <div class="icon"><svg width="34" height="30" viewBox="0 0 34 30"><path d="M2 28V12l8-6v6l8-6v6l8-6V2h4v26z" fill="var(--mid)"/></svg></div>
  <h3>Chimney Repairs</h3>
  <p>Lorem ipsum dolor sit amet, consectetur adipiscing elit. Etiam auctor tortor tellus, ut consectetur arcu. Nulla consequat egestas dapibus. Nullam eu quam sit amet justo imperdiet viverra. Vivamus leo lacus, interdum ac interdum</p>
</div>
<div class="abs service" style="left:455px;top:832px">
  <div class="icon"><svg width="32" height="28" viewBox="0 0 32 28"><path d="M2 8L16 2l14 6v18H2z" fill="var(--mid)"/><path d="M6 10h20v14H6z" fill="#fff" opacity=".5"/></svg></div>
  <h3>Ceilings</h3>
  <p>Lorem ipsum dolor sit amet, consectetur adipiscing elit. Etiam auctor tortor tellus, ut consectetur arcu. Nulla consequat egestas dapibus. Nullam eu quam sit amet justo imperdiet viverra. Vivamus leo lacus, interdum ac interdum</p>
</div>
<div class="abs service" style="left:786px;top:832px">
  <div class="icon"><svg width="30" height="30" viewBox="0 0 30 30"><path d="M2 2h26v10H14v16H2z" fill="var(--mid)"/></svg></div>
  <h3>Coving</h3>
  <p>Lorem ipsum dolor sit amet, consectetur adipiscing elit. Etiam auctor tortor tellus, ut consectetur arcu. Nulla consequat egestas dapibus. Nullam eu quam sit amet justo imperdiet viverra. Vivamus leo lacus, interdum ac interdum</p>
</div>
<div class="abs service" style="left:129px;top:1011px">
  <div class="icon"><svg width="34" height="34" viewBox="0 0 34 34"><rect x="9" y="2" width="16" height="30" rx="3" transform="rotate(45 17 17)" fill="var(--mid)"/></svg></div>
  <h3>Plasterboarding</h3>
  <p>Lorem ipsum dolor sit amet, consectetur adipiscing elit. Etiam auctor tortor tellus, ut consectetur arcu. Nulla consequat egestas dapibus. Nullam eu quam sit amet justo imperdiet viverra. Vivamus leo lacus, interdum ac interdum</p>
</div>
<div class="abs service" style="left:455px;top:1011px">
  <div class="icon"><svg width="34" height="34" viewBox="0 0 34 34"><path d="M4 24l14-14 6 6-14 14H4z M20 8l6-6 6 6-6 6" fill="none" stroke="var(--mid)" stroke-width="2"/></svg></div>
  <h3>Plastering</h3>
  <p>Lorem ipsum dolor sit amet, consectetur adipiscing elit. Etiam auctor tortor tellus, ut consectetur arcu. Nulla consequat egestas dapibus. Nullam eu quam sit amet justo imperdiet viverra. Vivamus leo lacus, interdum ac interdum</p>
</div>
<div class="abs service" style="left:786px;top:1011px">
  <div class="icon"><svg width="34" height="34" viewBox="0 0 34 34"><circle cx="17" cy="17" r="11" fill="none" stroke="var(--mid)" stroke-width="4" stroke-dasharray="5 3"/><circle cx="17" cy="17" r="5" fill="none" stroke="var(--mid)" stroke-width="2"/></svg></div>
  <h3>Rendering</h3>
  <p>Lorem ipsum dolor sit amet, consectetur adipiscing elit. Etiam auctor tortor tellus, ut consectetur arcu. Nulla consequat egestas dapibus. Nullam eu quam sit amet justo imperdiet viverra. Vivamus leo lacus, interdum ac interdum</p>
</div>

<section class="abs video-sec">
  <div class="abs video" role="img" aria-label="Gloved hand spreading plaster on a wall with a notched trowel">
    <div class="abs play"><svg width="14" height="16"><path d="M1 1l12 7-12 7z" fill="#fff"/></svg></div>
  </div>
  <h2>Lorem ipsum dolor sit amet, consectetur</h2>
  <p>Lorem ipsum dolor sit amet, consectetur adipiscing elit. Etiam auctor tortor tellus, ut consectetur arcu. Nulla consequat egestas dapibus. Nullam eu quam sit amet justo imperdiet viverra. Vivamus leo lacus, interdum ac interdum</p>
  <div class="quote-btn">A FREE QUOTE <svg width="14" height="8"><path d="M0 4h12M9 1l3 3-3 3" fill="none" stroke="#fff" stroke-width="1.5"/></svg></div>
</section>

<section class="abs work-sec">
  <h2 class="abs sec-title" style="top:46px">Recent work</h2>
  <p class="abs sec-lead" style="top:98px">Lorem ipsum dolor sit amet, consectetur adipiscing elit. Etiam auctor tortor tellus, ut<br>consectetur arcu. Nulla consequat egestas dapibus.</p>
  <div class="abs grid">
    <div role="img" aria-label="Tudor style house exterior" style="background:linear-gradient(#3a3a3a,#8a5a42)"></div>
    <div role="img" aria-label="Stone turret building under restoration" style="background:linear-gradient(#7d98b8,#8a7560)"></div>
    <div role="img" aria-label="Freshly plastered empty room with window" style="background:linear-gradient(#c9c9c6,#bfa27a)"></div>
    <div role="img" aria-label="Plasterer working on a ceiling" style="background:linear-gradient(#e9e6e0,#b79a70)"></div>
    <div role="img" aria-label="Loft room with roof window" style="background:linear-gradient(#eeeeee,#c59a62)"></div>
    <div role="img" aria-label="Bright hallway with orange ceiling feature" style="background:linear-gradient(120deg,#f2f2f2,#f06a1e 60%,#f4e4d0)"></div>
    <div role="img" aria-label="Room with pink curved ceiling" style="background:linear-gradient(#f3c8d6,#e46c8f)"></div>
    <div role="img" aria-label="White ceiling with skylights" style="background:linear-gradient(135deg,#e6e8ea,#b8bcc0)"></div>
  </div>
</section>

<div class="abs rule"></div>
<div class="abs partners-title"><span>WE’VE GOT YOU COVERED</span></div>
<div class="sq-btn" style="left:1002px;top:2425px"><svg width="7" height="10"><path d="M6 1L2 5l4 4" fill="none" stroke="#999"/></svg></div>
<div class="sq-btn" style="left:1044px;top:2425px"><svg width="7" height="10"><path d="M1 1l4 4-4 4" fill="none" stroke="#999"/></svg></div>
<div class="abs partner" style="left:140px"><i></i>Northgate Finishes</div>
<div class="abs partner" style="left:365px"><i></i>Ashcombe Homes</div>
<div class="abs partner" style="left:612px"><i></i>Meridian Works</div>
<div class="abs partner" style="left:866px"><i></i>Fenwick Plaster Co</div>

<section class="abs testi">
  <h2>Client Testimonials</h2>
  <p>Lorem ipsum dolor sit amet, consectetur adipiscing elit. Etiam auctor tortor tellus, ut consectetur arcu. Nulla consequat egestas dapibus. Nullam eu quam sit amet justo imperdiet viverra. Vivamus leo lacus, interdum ac interdum</p>
  <div class="who">- Harriet Lowe -</div>
  <div class="role">Founder, HLD Group</div>
  <div class="sq-btn" style="left:558px;top:236px"><svg width="7" height="10"><path d="M6 1L2 5l4 4" fill="none" stroke="#999"/></svg></div>
  <div class="sq-btn" style="left:600px;top:236px"><svg width="7" height="10"><path d="M1 1l4 4-4 4" fill="none" stroke="#999"/></svg></div>
</section>

<footer class="abs footer">
  <h4 style="left:130px">Menu</h4>
  <h4 style="left:338px">Latest Posts</h4>
  <h4 style="left:626px">Recent Tweets</h4>
  <h4 style="left:915px">Contact Information</h4>
  <div class="f-menu">Home<br>About<br>&nbsp;Services<br>News &amp; Updates<br>Contact us<br>Help</div>
  <div class="post" style="top:98px"><i role="img" aria-label="Post thumbnail of an orange interior" style="background:linear-gradient(#f3f3f3,#e9792f)"></i><span>Lorem ipsum dolor sit amet, consectetur adipiscing elit.</span></div>
  <div class="post" style="top:186px"><i role="img" aria-label="Post thumbnail of a loft room" style="background:linear-gradient(#f0f0f0,#c7a57a)"></i><span>Etiam auctor tortor tellus, ut consectetur arcu.</span></div>
  <div class="post" style="top:274px"><i role="img" aria-label="Post thumbnail of plastering work" style="background:linear-gradient(#b48a5a,#e6dccb)"></i><span>Nullam eu quam sit amet justo imperdiet viverra. Vivamus leo lacus,</span></div>
  <div class="tweets">
    <div class="top">What's being said about...</div>
    <div class="name">Brookvale Rendering</div>
    <ul>
      <li><i></i><div><b>tomwalbrook</b> Reading @brookvalerender<br>15 hours ago</div></li>
      <li><i></i><div><b>kerrybell</b> The 10 county rendering Read you @brookvalerender<br>9 hours ago</div></li>
      <li><i></i><div><b>oakroomstudio</b> @brookvalerender Thanks for the follow - hope<br>5 hours ago</div></li>
    </ul>
    <div class="bottom"><span>Tweets</span><span>Join the conversation</span></div>
  </div>
  <div class="contact">Lorem ipsum, dolor<br>sit amer, United Kingdom<br><br>t: 01632 960 457<br>e: hello@brookvalerendering.co.uk</div>
  <div class="copy">©2016 BrookvaleRendering.com All Rights reserved</div>
</footer>

</body>
</html>
```